Screen design for customizable PARISH LINK

I am building a customizable app for churches. I need the following screens designed:
1) Landing Screen
-- Text field to enter a code to join a organization
-- Button to register a new organization
2) Registration Screen
-- Text field to enter an organization name
-- Register button
-- Screen should indicate price/month and free trial for X days
3) Restricted (requires login) screen
4) Organization home screen
-- Dynamic menu options of the following types:
a) Contact Us/Form
b) Video List
c) Audio List
d) Documents List
e) Message/Chat Rooms
f) Map/Directions
g) Webpage

Plus permission based options:
h) Profile Settings
i) Notification Center
j) Admin Settings
k) Manage members
l) View Form Submissions

Low-fi/wireframe designs attached. No color scheme or branding has been established yet.

```html
<!DOCTYPE html>
<html lang="en">
<head>
<meta charset="utf-8">
<title>Parish Link – App Screens</title>
<link href="https://fonts.googleapis.com/css2?family=Poppins:wght@400;500;600&display=swap" rel="stylesheet">
<style>
:root{
  --navy:#213f86;
  --navy-light:#35599f;
  --navy-btn:#164c93;
  --navy-btn-dark:#173a78;
  --gold:#d0b05f;
  --gold-dark:#a98444;
  --ink:#1d3a7a;
  --grey:#8a8f99;
  --line:#c9ccd2;
  --white:#ffffff;
}
*{box-sizing:border-box;margin:0;padding:0}
html,body{width:1200px;height:2517px;overflow:hidden;background:var(--white);font-family:"Poppins",sans-serif}
.canvas{position:relative;width:1200px;height:2517px;overflow:hidden}
.backdrop{position:absolute;left:0;top:0}
.phone{position:absolute;width:322px;height:572px;border-radius:30px;overflow:hidden;background:var(--white);box-shadow:0 14px 30px rgba(20,30,60,.18)}
.phone--blue{background:linear-gradient(180deg,var(--navy-light),var(--navy))}
.splash{left:439px;top:224px}
.landing{left:67px;top:874px}
.login{left:439px;top:969px}
.register{left:810px;top:1042px}
.home{left:439px;top:1714px}
.app-bar{position:absolute;left:0;top:0;width:100%;height:50px;background:linear-gradient(180deg,var(--navy-light),var(--navy))}
.app-bar svg{position:absolute;top:14px}
.wordmark{position:absolute;left:0;width:100%;text-align:center;font-weight:600;letter-spacing:.5px;color:var(--ink);font-size:17px}
.wordmark--light{color:var(--white);font-size:26px}
.field{position:absolute;height:37px;border:1px solid var(--line);font-size:10px;color:var(--grey);padding-left:12px;line-height:35px}
.btn{position:absolute;height:37px;background:linear-gradient(90deg,var(--navy-btn),var(--navy-btn-dark));color:var(--white);font-size:12.5px;text-align:center;line-height:37px}
.label{position:absolute;font-size:10.5px;font-weight:500;color:var(--ink)}
.small{position:absolute;left:0;width:100%;text-align:center;font-size:8.5px;color:#4a4f5a}
.small a{color:var(--navy-btn);text-decoration:none}
.join-card{position:absolute;left:45px;top:124px;width:234px;height:321px;background:var(--white);border-radius:10px}
.icon-artwork{position:absolute;left:49px;top:268px;width:232px;height:304px;border-radius:116px 116px 0 0;background:radial-gradient(circle at 50% 22%,#e6c16b 0,#c99a44 22%,#6b3a1c 45%,#2f2a1c 75%)}
.menu{position:absolute;left:0;top:144px;width:100%}
.menu-item{position:absolute;width:96px;text-align:center;font-size:9.5px;line-height:10px;color:#4a4f5a}
.menu-item svg{display:block;margin:0 auto 8px;width:32px;height:32px;fill:none;stroke:var(--ink);stroke-width:1.6;stroke-linecap:round;stroke-linejoin:round}
.menu-item--active{color:var(--gold-dark)}
.menu-item--active svg{stroke:var(--gold-dark)}
.tab-bar{position:absolute;left:0;top:531px;width:100%;height:41px;border-top:1px solid #e4e6ea;background:var(--white)}
.tab-bar svg{position:absolute;top:11px;width:18px;height:18px;fill:none;stroke:#c3c6cc;stroke-width:1.4}
</style>
</head>
<body>
<div class="canvas">
  <svg class="backdrop" width="1200" height="2517" viewBox="0 0 1200 2517">
    <defs>
      <linearGradient id="bulbGrad" gradientUnits="userSpaceOnUse" x1="0" y1="90" x2="0" y2="485">
        <stop offset="0" stop-color="#d2b262"/><stop offset="1" stop-color="#a98444"/>
      </linearGradient>
      <linearGradient id="goldGrad" x1="0" y1="0" x2="0" y2="1">
        <stop offset="0" stop-color="#d0b05f"/><stop offset="1" stop-color="#a98444"/>
      </linearGradient>
      <linearGradient id="goldBand" x1="1" y1="0" x2="0" y2="1">
        <stop offset="0" stop-color="#cfae5e"/><stop offset="1" stop-color="#b08c4a"/>
      </linearGradient>
      <linearGradient id="blueGrad" x1="0" y1="0" x2="0" y2="1">
        <stop offset="0" stop-color="#35599f"/><stop offset="1" stop-color="#213f86"/>
      </linearGradient>
    </defs>
    <g class="bulb" fill="url(#bulbGrad)">
      <circle cx="381" cy="227" r="137"/>
      <path d="M262 294 C290 330 310 350 315 385 Q318 408 342 408 L470 408 L470 250 Z"/>
      <rect x="317" y="443" width="150" height="40" rx="12"/>
    </g>
    <circle cx="758" cy="796" r="111" fill="url(#goldGrad)"/>
    <path d="M0 1025 C150 940 330 900 520 960 L760 1075 L1200 740 L1200 1245 L1130 1310 L1130 1560 C900 1560 760 1540 620 1500 C450 1480 350 1530 300 1600 C220 1720 100 1960 0 2165 Z" fill="url(#goldBand)"/>
    <circle cx="759" cy="2189" r="186" fill="url(#blueGrad)"/>
  </svg>

  <section class="phone phone--blue splash" role="img" aria-label="Splash screen over a faint photo of a gothic cathedral vault">
    <div class="wordmark wordmark--light" style="top:303px">PARISH LINK</div>
  </section>

  <section class="phone phone--blue landing" role="img" aria-label="Landing screen over a faint cathedral vault photo">
    <div class="join-card">
      <div class="wordmark" style="top:95px">PARISH LINK</div>
      <div class="label" style="left:23px;top:172px">Join an organization</div>
      <div class="field" style="left:23px;top:192px;width:188px">Enter code</div>
      <div class="btn" style="left:23px;top:239px;width:188px;font-size:10.5px">Register an organization</div>
    </div>
  </section>

  <section class="phone login">
    <div class="app-bar"></div>
    <div class="wordmark" style="top:191px">PARISH LINK</div>
    <div class="field" style="left:36px;top:262px;width:250px">Username</div>
    <div class="field" style="left:36px;top:307px;width:250px">Password</div>
    <div class="btn" style="left:36px;top:358px;width:250px">Sign In</div>
    <p class="small" style="top:416px">ForgotPassword? <a>Click here</a></p>
    <p class="small" style="top:439px">Dont have account? <a>Create Account</a></p>
  </section>

  <section class="phone register">
    <div class="app-bar">
      <svg style="left:18px" width="16" height="22" viewBox="0 0 16 22"><path d="M12 2 L3 11 L12 20" fill="none" stroke="#fff" stroke-width="2.4" stroke-linecap="round"/></svg>
    </div>
    <div class="label" style="left:35px;top:106px">Church name</div>
    <div class="field" style="left:35px;top:127px;width:251px">Enter name</div>
    <div class="btn" style="left:35px;top:175px;width:251px">Register</div>
    <p class="small" style="top:226px">$3.20 price/month &amp; free trial for X days</p>
    <div class="icon-artwork" role="img" aria-label="Religious icon painting with golden halo"></div>
  </section>

  <section class="phone home">
    <div class="app-bar">
      <svg style="left:18px" width="16" height="22" viewBox="0 0 16 22"><path d="M12 2 L3 11 L12 20" fill="none" stroke="#fff" stroke-width="2.4" stroke-linecap="round"/></svg>
      <svg style="right:18px;top:15px" width="22" height="20" viewBox="0 0 22 20"><path d="M1 2H21M1 10H21M1 18H21" stroke="#fff" stroke-width="2.4" stroke-linecap="round"/></svg>
    </div>
    <div class="menu">
      <div class="menu-item" style="left:17px;top:0"><svg viewBox="0 0 32 32"><path d="M6 8c-2 3 0 9 6 15s12 8 15 6l-1-5-5-1-2 3c-3-1-7-5-8-8l3-2-1-5z"/><rect x="15" y="3" width="13" height="10" rx="3"/><path d="M19 8h.1M22 8h.1M25 8h.1"/></svg>Contact Us</div>
      <div class="menu-item menu-item--active" style="left:113px;top:0"><svg viewBox="0 0 32 32"><rect x="4" y="4" width="24" height="18" rx="2"/><path d="M13 9v8l7-4z"/><path d="M4 27h24M10 27v-2"/></svg>Video List</div>
      <div class="menu-item" style="left:209px;top:0"><svg viewBox="0 0 32 32"><path d="M4 14v4M9 8v16M14 4v24M19 10v12M24 6v20M28 13v6"/></svg>Audio List</div>

      <div class="menu-item" style="left:17px;top:85px"><svg viewBox="0 0 32 32"><path d="M8 3h13l5 5v20H8z"/><path d="M12 11h10M12 16h10M12 21h5"/><path d="M20 26l7-7 2 2-7 7h-2z"/></svg>Documents<br>List</div>
      <div class="menu-item" style="left:113px;top:85px"><svg viewBox="0 0 32 32"><path d="M5 6h22v15H13l-6 5v-5H5z"/><path d="M11 12h10M11 16h10"/></svg>Message/<br>Chat Rooms</div>
      <div class="menu-item" style="left:209px;top:85px"><svg viewBox="0 0 32 32"><rect x="4" y="4" width="24" height="24"/><path d="M4 4l24 24M28 4l-10 10"/><circle cx="11" cy="21" r="3"/></svg>Map/<br>Directions</div>

      <div class="menu-item" style="left:17px;top:174px"><svg viewBox="0 0 32 32"><rect x="3" y="5" width="26" height="22" rx="1"/><path d="M3 10h26M6 7.5h.1M9 7.5h.1"/><path d="M7 15h3M13 15h12M7 19h3M13 19h12M7 23h3M13 23h12"/></svg>Webpage</div>
      <div class="menu-item" style="left:113px;top:174px"><svg viewBox="0 0 32 32"><path d="M16 3l3 3h4v4l3 3-3 3v4h-4l-3 3-3-3H9v-4l-3-3 3-3V6h4z"/><circle cx="16" cy="12" r="3"/><path d="M11 19c1-3 9-3 10 0"/></svg>Profile<br>Settings</div>
      <div class="menu-item" style="left:209px;top:174px"><svg viewBox="0 0 32 32"><path d="M16 3l3 3h4v4l3 3-3 3v4h-4l-3 3-3-3H9v-4l-3-3 3-3V6h4z"/><circle cx="16" cy="13" r="6"/><path d="M16 10v3M16 16h.1"/></svg>Notification<br>Settings</div>

      <div class="menu-item" style="left:17px;top:264px"><svg viewBox="0 0 32 32"><path d="M16 3l3 3h4v4l3 3-3 3v4h-4l-3 3-3-3H9v-4l-3-3 3-3V6h4z"/><circle cx="16" cy="13" r="3"/><path d="M16 16v12M13 25h6"/></svg>Admin<br>Settings</div>
      <div class="menu-item" style="left:113px;top:264px"><svg viewBox="0 0 32 32"><circle cx="16" cy="9" r="4"/><circle cx="8" cy="13" r="3"/><circle cx="24" cy="13" r="3"/><path d="M9 27v-6a7 7 0 0 1 14 0v6zM3 27v-5a5 5 0 0 1 6-4M29 27v-5a5 5 0 0 0-6-4"/></svg>Manage<br>members</div>
      <div class="menu-item" style="left:209px;top:264px"><svg viewBox="0 0 32 32"><path d="M7 3h15l4 4v9M7 3v25h9"/><path d="M11 10h10M11 14h8"/><circle cx="22" cy="20" r="3"/><path d="M16 29c0-4 12-4 12 0"/></svg>View Form<br>Submissions</div>
    </div>
    <nav class="tab-bar">
      <svg style="left:84px" viewBox="0 0 18 18"><path d="M2 8L9 2l7 6v8H2z"/><path d="M7 16v-5h4v5"/></svg>
      <svg style="left:152px" viewBox="0 0 18 18"><path d="M4 13V8a5 5 0 0 1 10 0v5l1.5 1.5h-15zM7.5 16h3"/></svg>
      <svg style="left:222px" viewBox="0 0 18 18"><circle cx="9" cy="6" r="3.5"/><path d="M3 17c0-4 12-4 12 0"/></svg>
    </nav>
  </section>
</div>
</body>
</html>
```